QRV MOONLIT GLOW Party

Hi,
Want to design a flyer for a party.

I have attached a design I would like you to work from and just add in the correct text:

QRV Events presents

November 2013

MOONLIT GLOW
PARTY

DJ COPPER LANTERN
VENUE: TBA

DOORS OPEN 8PM

ENTRY STRICTLY OVER 18'S.

DRESS CODE: SMART CASUAL SULTRY SEXY SPRING THREADS

COST: $60 PER HEAD, includes champagne, beer & wine and canapes.

Tickets from www.quietrivervista.com.au or 0491 570 156.

```html
<!DOCTYPE html>
<html lang="en">
<head>
<meta charset="utf-8">
<title>Moonlit Glow Party – QRV Events</title>
<link rel="stylesheet" href="https://fonts.googleapis.com/css2?family=Montserrat:wght@200;300;700;900&family=Michroma&family=Arimo:wght@400;700&display=swap">
<style>
  :root {
    --ink: #050506;
    --night: #141418;
    --silver-hi: #ffffff;
    --silver-mid: #b9bcc2;
    --silver-lo: #6d7078;
    --pink: #d6348f;
    --white: #f4f4f4;
    --glow: #cfe4ff;
    --gold: #b08a3e;
  }
  * { margin: 0; padding: 0; box-sizing: border-box; }
  html, body { width: 798px; height: 1200px; overflow: hidden; background: var(--ink); }
  .flyer {
    position: relative;
    width: 798px; height: 1200px;
    background: radial-gradient(ellipse at 50% 45%, #23232a 0%, var(--night) 45%, var(--ink) 100%);
    color: var(--white);
    font-family: "Arimo", Arial, sans-serif;
    overflow: hidden;
  }
  .trim {
    position: absolute; left: 0; width: 100%; height: 14px;
    background: linear-gradient(180deg, var(--silver-lo), var(--silver-hi) 45%, var(--silver-mid) 70%, var(--silver-lo));
  }
  .trim--top { top: 0; }
  .trim--bottom { bottom: 0; }
  .vip-ribbon { position: absolute; top: 0; right: 0; width: 150px; height: 150px; }
  .presenter {
    position: absolute; top: 100px; width: 100%; text-align: center;
    font-family: "Michroma", sans-serif; font-size: 20px; letter-spacing: 1px;
  }
  .presenter strong { font-family: "Montserrat", sans-serif; font-weight: 900; letter-spacing: 2px; }
  .presenter-rule {
    position: absolute; top: 134px; left: 230px; width: 338px; height: 2px;
    background: linear-gradient(90deg, transparent, var(--glow), transparent);
  }
  .event-date {
    position: absolute; top: 150px; width: 100%; text-align: center;
    font-family: "Montserrat", sans-serif; font-weight: 900; font-size: 28px; letter-spacing: 3px;
  }
  .hero-art {
    position: absolute; top: 200px; left: 40px; width: 718px; height: 560px;
    background:
      radial-gradient(ellipse at 50% 40%, rgba(220,225,235,0.55) 0%, rgba(140,150,170,0.35) 30%, rgba(40,40,50,0.2) 60%, transparent 75%),
      radial-gradient(ellipse at 50% 20%, rgba(190,150,90,0.35) 0%, transparent 40%);
  }
  .title {
    position: absolute; left: 0; width: 100%; text-align: center;
    font-family: "Montserrat", sans-serif; line-height: 1;
    background: linear-gradient(180deg, var(--silver-hi) 0%, var(--silver-mid) 48%, var(--silver-lo) 52%, var(--silver-hi) 100%);
    -webkit-background-clip: text; background-clip: text; color: transparent;
  }
  .title--main { top: 772px; font-weight: 900; font-size: 66px; letter-spacing: -1px; }
  .title--sub { top: 842px; font-weight: 200; font-size: 76px; letter-spacing: 6px; }
  .headliner {
    position: absolute; top: 936px; width: 100%; text-align: center;
    font-family: "Montserrat", sans-serif; font-weight: 300; font-size: 36px; letter-spacing: 2px;
    color: var(--pink);
  }
  .headliner-rule { position: absolute; top: 982px; left: 102px; width: 594px; height: 1px; background: var(--silver-mid); }
  .venue { position: absolute; top: 992px; width: 100%; text-align: center; font-weight: 700; font-size: 17px; }
  .venue .sep { color: var(--pink); padding: 0 10px; font-weight: 400; }
  .details { position: absolute; top: 1026px; left: 0; width: 100%; height: 90px; font-size: 18px; }
  .details-col { position: absolute; top: 0; line-height: 25px; }
  .details-col--dress { right: 413px; text-align: right; }
  .details-col--cost { left: 420px; }
  .details-divider { position: absolute; top: 2px; left: 399px; width: 2px; height: 82px; background: var(--pink); }
  .label { color: var(--pink); }
  .age-note { position: absolute; top: 1122px; width: 100%; text-align: center; font-size: 17px; color: var(--pink); }
  .tickets-label { position: absolute; top: 1134px; left: 22px; font-size: 17px; color: var(--pink); }
  .contact { position: absolute; top: 1158px; left: 22px; right: 22px; font-weight: 700; font-size: 22px; display: flex; justify-content: space-between; }
</style>
</head>
<body>
<main class="flyer">
  <div class="trim trim--top"></div>

  <svg class="vip-ribbon" viewBox="0 0 150 150" aria-hidden="true">
    <polygon points="40,0 80,0 150,70 150,110" fill="#121214"/>
    <line x1="40" y1="0" x2="150" y2="110" stroke="#b08a3e" stroke-width="2"/>
    <line x1="80" y1="0" x2="150" y2="70" stroke="#b08a3e" stroke-width="2"/>
    <text x="112" y="56" fill="#c9a45a" font-family="Georgia, serif" font-size="13" transform="rotate(45 112 56)" text-anchor="middle">VIP</text>
  </svg>

  <p class="presenter">QRV EVENTS <strong>PRESENTS</strong></p>
  <div class="presenter-rule"></div>
  <p class="event-date">NOVEMBER 2013</p>

  <div class="hero-art" role="img" aria-label="Woman in a white halter gown seated before a mirror disco ball, gilded crown frame, speakers and two white doves"></div>

  <h1 class="title title--main">MOONLIT GLOW</h1>
  <p class="title title--sub">PARTY</p>

  <p class="headliner">DJ COPPER LANTERN</p>
  <div class="headliner-rule"></div>
  <p class="venue">VENUE: TBA<span class="sep">|</span>DOORS OPEN 8PM</p>

  <section class="details">
    <div class="details-col details-col--dress">
      <span class="label">DRESS CODE:</span><br>
      SMART CASUAL SULTRY<br>SEXY SPRING THREADS
    </div>
    <div class="details-divider"></div>
    <div class="details-col details-col--cost">
      <span class="label">COST:</span> $60 PER HEAD<br>
      INCLUDES CHAMPAGNE,<br>BEER &amp; WINE AND CANAPES.
    </div>
  </section>

  <p class="age-note">ENTRY STRICTLY OVER 18'S.</p>
  <p class="tickets-label">Tickets from:</p>
  <p class="contact"><span>www.QUIETRIVERVISTA.com.au</span><span>ph: 0491 570 156</span></p>

  <div class="trim trim--bottom"></div>
</main>
</body>
</html>
```